QRDKS Updated logo business card

Can you create a new business card with our new logo? I have included a rough mockup of what our team thought of. I would need this as a background image to purchase cards via Norvellex.

Contact Information for Business Card

Title, name,

```html
<!DOCTYPE html>
<html lang="en">
<head>
<meta charset="UTF-8">
<title>QRDKS Business Card</title>
<link rel="stylesheet" href="https://fonts.googleapis.com/css2?family=Oswald:wght@400;500;700&display=swap">
<style>
  :root {
    --canvas-bg: #ebebeb;
    --card-red: #9c1b3b;
    --card-yellow: #ecb01e;
    --paper: #ffffff;
    --ink-red: #9c1b3b;
    --ink-grey: #8a8a8a;
    --ink-dark: #2a2a2a;
    --ink-pink: #e7a9b8;
  }
  * { margin: 0; padding: 0; box-sizing: border-box; }
  html, body {
    width: 800px;
    height: 1200px;
    overflow: hidden;
    background: var(--canvas-bg);
    font-family: "Oswald", sans-serif;
  }
  .sheet {
    position: relative;
    width: 800px;
    height: 1200px;
  }
  .card {
    position: absolute;
    left: 80px;
    width: 640px;
    height: 366px;
    overflow: hidden;
    box-shadow: 0 6px 18px rgba(0, 0, 0, 0.12);
  }
  .card-front { top: 170px; background: var(--card-red); }
  .card-back  { top: 664px; background: var(--card-yellow); }

  .name-plate {
    position: absolute;
    left: 220px;
    right: 0;
    top: 108px;
    height: 96px;
    background: var(--paper);
    padding: 14px 0 0 0;
    text-align: right;
    padding-right: 28px;
  }
  .name-plate .person-name {
    display: block;
    font-weight: 500;
    font-size: 40px;
    line-height: 44px;
    color: var(--ink-red);
    letter-spacing: 0.5px;
  }
  .name-plate .person-title {
    display: block;
    font-weight: 400;
    font-size: 19px;
    line-height: 24px;
    color: var(--ink-grey);
    letter-spacing: 1px;
  }
  .front-footer {
    position: absolute;
    left: 26px;
    bottom: 26px;
    font-size: 9px;
    line-height: 13px;
    letter-spacing: 0.8px;
    color: var(--ink-pink);
  }

  .logo-plate {
    position: absolute;
    left: 0;
    top: 142px;
    width: 400px;
    height: 100px;
    background: var(--paper);
    display: flex;
    align-items: center;
    gap: 14px;
    padding-left: 36px;
  }
  .logo-plate .brand-mark {
    width: 26px;
    height: 26px;
    background: var(--card-red);
  }
  .logo-plate .brand-name {
    font-weight: 700;
    font-size: 52px;
    line-height: 1;
    color: var(--ink-dark);
    letter-spacing: 2px;
  }
</style>
</head>
<body>
  <main class="sheet">
    <section class="card card-front" aria-label="Business card front">
      <div class="name-plate">
        <span class="person-name">YOUR NAME</span>
        <span class="person-title">POSITION</span>
      </div>
      <div class="front-footer">
        <p>QRDKS BUILDING MATERIALS</p>
        <p>SUPPLY ASSOCIATION</p>
      </div>
    </section>

    <section class="card card-back" aria-label="Business card back">
      <div class="logo-plate">
        <span class="brand-mark" aria-hidden="true"></span>
        <span class="brand-name">QRDKS</span>
      </div>
    </section>
  </main>
</body>
</html>
```